Trucking Insurance Website Design

We are working with a Trucking Insurance company in California. They provide vehicle insurance for trucking companies and truckers.
As you might imagine, there are no websites we could find for inspiration for trucking insurance. But below are sites that do similar insurance.
https://brindlemorecover.com/trucking-insurance/
https://www.haulwardpolicy.com/california-commercial-truck-insurance
Thank you for taking the time to consider designing a website for us. We are web developers based in Stockton, CA, USA. Most of our projects go through the same process. Understanding this process may help you win a project with us. We custom-code all of our websites in-house. We don’t have any requirements as to what tools you use for your design, but we ask that you follow these guidelines.
IMAGES:
If you use any images or icons in the design, we ask that you have a link to the asset so we can purchase the image/icon. Most of the designs we submit do not have the customer’s images on them unless they have some great images. Be creative; show us the feeling you are trying to portray with your image choices. Use any royalty-free site you choose. We subscribe to Quillen and mainly use their images, but we can purchase images outside of Quillen. PLEASE NOTE: we will not submit designs to clients with watermarks on the images.
FONTS:
We ask that you identify the fonts you’re using in the design. This can be done in a message if you want. We typically use Marlowe Type and Quillen Type.
CONTENT:
We're always open to different content and ideas. We often submit designs with stock images so the client can see our vision. We typically take pictures after the website launch to use their images with our vision. Lorem Ipsum is fine for paragraphs, but we ask that you make the Headers with correct English. We want to be able to show the vision and identify the sections of the website.
INSPIRATION:
We typically add a couple of links in the brief of websites we like to help you get started in your design.
REVISIONS:
We do not often ask for revisions of the designs unless we see something in the design that may not appeal to the client. If there are slight changes that we want to make, we do that in the development process.
FEEDBACK:
We rarely give feedback on designs during the design process. We are working on many website projects and do not have the time to provide feedback. We usually respond if your request is well thought out and asks specific questions, but a note asking “feedback, please” usually goes unanswered.
1 page

```html
<!DOCTYPE html>
<html lang="en">
<head>
<meta charset="utf-8">
<title>Tarrowby Insurance — Commercial Truck Insurance</title>
<link href="https://fonts.googleapis.com/css2?family=Arimo:wght@400;700&display=swap" rel="stylesheet">
<style>
:root{
  --red:#c8102e;
  --red-dark:#9e0f22;
  --blue:#2f3b8f;
  --blue-mid:#3d4aa5;
  --ink:#222;
  --muted:#555;
  --grey-bg:#f0f0f0;
  --field:#f1f2f4;
  --footer:#1d2524;
  --pink:#f4c6cd;
  --white:#fff;
}
*{box-sizing:border-box;margin:0;padding:0}
html,body{width:1200px;height:4910px;overflow:hidden}
body{position:relative;font-family:"Arimo",Arial,sans-serif;color:var(--ink);background:var(--white)}
.abs{position:absolute}
.btn{position:absolute;display:inline-block;border-radius:26px;color:var(--white);font-weight:700;font-size:14px;text-transform:uppercase;text-align:center;line-height:50px;height:50px;background:linear-gradient(90deg,var(--red-dark),var(--red));box-shadow:0 4px 8px rgba(0,0,0,.2)}
.photo{position:absolute;overflow:hidden}

/* header */
.site-header{position:absolute;left:0;top:0;width:1200px;height:130px}
.brand{position:absolute;display:flex;align-items:center;gap:10px;font-weight:700;color:var(--blue);letter-spacing:2px}
.brand .dot{width:34px;height:34px;border-radius:50%;background:var(--red)}
.main-nav{position:absolute;left:476px;top:92px;display:flex;gap:40px;font-size:13px;color:#333}
.main-nav a{color:inherit;text-decoration:none}
.pill{position:absolute;top:34px;height:38px;line-height:38px;border-radius:19px;color:#fff;font-size:13px;font-weight:700;text-align:center}
.pill.pay{left:764px;width:100px;background:var(--blue-mid)}
.pill.quote{left:874px;width:176px;background:var(--red)}

/* hero */
.hero{position:absolute;left:0;top:130px;width:1200px;height:805px}
.hero-copy{position:absolute;right:148px;top:570px;text-align:right;color:#fff}
.hero-copy h1{font-size:39px;font-weight:400;letter-spacing:.5px}
.hero-copy p{font-size:20px;line-height:24px;margin-top:8px}
.arrow{position:absolute;width:24px;height:24px}

/* welcome */
.section-title{position:absolute;left:0;width:1200px;text-align:center}
.eyebrow{color:var(--red);font-weight:700;font-size:30px}
.headline{color:var(--blue);font-weight:700;font-size:39px;margin-top:6px}
.service{position:absolute;top:1180px;width:250px;text-align:center}
.service .ring{position:relative;width:250px;height:250px}
.service .ring .flag{position:absolute;right:0;top:0;width:58px;height:58px;background:var(--red)}
.service .ring .circle{position:absolute;left:0;top:0;width:248px;height:248px;border-radius:50%;border:3px solid var(--red);background:#fff}
.service .ring .img{position:absolute;left:16px;top:16px;width:216px;height:216px;border-radius:50%}
.service h3{font-size:17px;margin-top:20px}
.service p{font-size:13px;line-height:17px;color:var(--muted);margin-top:14px}
.dots{position:absolute;top:1588px;left:568px;display:flex;gap:12px}
.dots i{width:14px;height:14px;border-radius:50%;background:#888;display:block}
.dots i.on{background:var(--red)}

/* about */
.about-copy{position:absolute;left:150px;top:1830px;width:380px}
.about-copy h2{font-size:38px;line-height:46px;color:var(--blue)}
.about-copy h2 .r{color:var(--red)}
.about-copy p{font-size:14px;line-height:18px;color:var(--muted);margin-top:30px}
.corner{position:absolute;width:62px;height:60px;background:var(--red);clip-path:polygon(0 0,100% 0,100% 100%)}

/* why */
.why-copy{position:absolute;left:148px;top:2490px;width:340px}
.why-copy .label{color:var(--red);font-weight:700;font-size:24px}
.why-copy h2{color:var(--blue);font-size:38px;line-height:46px;margin-top:20px}
.feature{position:absolute;width:260px;text-align:center}
.feature svg{width:44px;height:44px}
.feature h3{font-size:21px;margin-top:8px}
.feature p{font-size:14px;line-height:18px;color:var(--muted);margin-top:8px}

/* quote */
.quote-band{position:absolute;left:0;top:2956px;width:1200px;height:658px}
.quote-band h2{position:absolute;left:148px;top:3175px;color:#fff;font-size:40px;line-height:50px;text-transform:uppercase;width:420px}
.quote-form{position:absolute;left:644px;top:3040px;width:409px;height:475px;background:#fff}
.quote-form .head{height:70px;background:var(--red);color:#fff;font-weight:700;font-size:21px;text-align:center;line-height:80px}
.field{position:absolute;left:34px;width:341px;height:42px;background:var(--field);font-size:10px;color:#555;padding:14px 12px}
.field.msg{height:101px}
.submit{position:absolute;left:137px;top:414px;width:133px;height:38px;line-height:38px;border-radius:19px;background:var(--blue);color:#fff;font-size:13px;font-weight:700;text-align:center}

/* blog */
.blog-title{position:absolute;left:0;top:3745px;width:1200px;text-align:center;color:var(--red);font-size:38px;font-weight:700}
.blog-feature h3{position:absolute;left:150px;top:4228px;width:400px;font-size:27px;font-weight:400;line-height:32px;color:#666}
.date{color:var(--red);font-weight:700;font-size:13px}
.post{position:absolute;left:575px;width:470px;height:134px;border-bottom:2px solid #ccc}
.post .thumb{position:absolute;left:0;top:0;width:162px;height:133px}
.post h4{position:absolute;left:188px;top:20px;font-size:20px;font-weight:400;line-height:26px;color:#333}
.post .date{position:absolute;left:196px;top:88px}

/* footer */
.site-footer{position:absolute;left:0;top:4380px;width:1200px;height:530px}
.foot-col{position:absolute;top:4600px;color:#fff}
.foot-col h5{font-size:16px;font-weight:700;margin-bottom:16px}
.foot-col li{list-style:none;font-size:12px;line-height:23px;color:#ddd}
.contact-row{display:flex;gap:14px;margin-bottom:16px;font-size:12px;line-height:15px;color:#ddd}
.contact-row .ico{flex:none;width:34px;height:34px;border-radius:50%;background:var(--red);display:flex;align-items:center;justify-content:center}
.social{position:absolute;top:4846px;display:flex;gap:10px;left:152px}
.social i{display:block;width:40px;height:40px;border-radius:50%;border:2px solid #fff}
</style>
</head>
<body>

<header class="site-header">
  <div class="brand" style="left:152px;top:36px;font-size:17px"><span class="dot"></span>TARROWBY INSURANCE</div>
  <a class="pill pay">PAY NOW</a>
  <a class="pill quote">REQUEST A QUOTE</a>
  <nav class="main-nav">
    <a>Home</a><a>About Us</a><a>Truck Insurance</a><a>Why Chose Us?</a><a>Blog</a><a>Contact</a>
  </nav>
</header>

<section class="hero">
  <div class="photo" role="img" aria-label="Woman in red vest holding a tablet in front of a row of blue trucks" style="left:0;top:0;width:1200px;height:805px;background:linear-gradient(160deg,#1d2d8a 0%,#3a4fb0 30%,#8d96a8 55%,#c7c9cf 75%,#8a2030 100%)"></div>
  <svg class="abs" style="left:0;top:0" width="1200" height="805" viewBox="0 0 1200 805">
    <path d="M0 600 C160 660 430 770 800 792 L1200 770 L1200 805 L0 805 Z" fill="#fff"/>
    <path d="M0 270 C110 500 390 730 800 792 C420 770 160 660 0 600 Z" fill="#c8102e"/>
    <path d="M230 530 C520 590 900 520 1200 370 L1200 800 C1050 815 920 810 800 792 C560 750 370 650 230 530 Z" fill="#3442a0"/>
  </svg>
  <svg class="arrow" style="left:80px;top:205px" viewBox="0 0 24 24"><path d="M16 3 L7 12 L16 21" stroke="#fff" stroke-width="3" fill="none"/></svg>
  <svg class="arrow" style="left:1132px;top:245px" viewBox="0 0 24 24"><path d="M8 3 L17 12 L8 21" stroke="#fff" stroke-width="3" fill="none"/></svg>
  <div class="hero-copy">
    <h1>TARROWBY INSURANCE</h1>
    <p>Lorem ipsum dolor sit amet, consectetur adipis<br>eiusmod tempor incididunt ut labore</p>
  </div>
  <a class="btn" style="left:866px;top:690px;width:184px">Request a quote</a>
</section>

<section class="welcome">
  <div class="section-title" style="top:1015px">
    <div class="eyebrow">WELCOME TO</div>
    <div class="headline">TARROWBY INSURANCE</div>
  </div>
  <div class="service" style="left:152px">
    <div class="ring"><span class="flag"></span><span class="circle"></span><span class="img" role="img" aria-label="Trucker smiling while using a tablet beside his truck" style="background:linear-gradient(135deg,#d8dde4,#7b8aa0)"></span></div>
    <h3>Tractor Trailer Insurance</h3>
    <p>Lorem ipsum dolor sit amet, con sectetur adipiscing elit, sed do eiul ou esmod tempor incididunt ut lab ore et dolore magna aliqua.</p>
  </div>
  <div class="service" style="left:475px">
    <div class="ring"><span class="flag"></span><span class="circle"></span><span class="img" role="img" aria-label="Red semi truck on a highway at sunset" style="background:linear-gradient(180deg,#e7b27a,#b33a2a 60%,#4a4a4a)"></span></div>
    <h3>Dump Truck Insurance</h3>
    <p>Lorem ipsum dolor sit amet, con sectetur adipiscing elit, sed do eiul ou esmod tempor incididunt ut lab ore et dolore magna aliqua.</p>
  </div>
  <div class="service" style="left:800px">
    <div class="ring"><span class="flag"></span><span class="circle"></span><span class="img" role="img" aria-label="Overturned box truck lying in a field" style="background:linear-gradient(180deg,#9bb4d0,#d9dde2 50%,#7f8a55)"></span></div>
    <h3>Box Truck Insurance</h3>
    <p>Lorem ipsum dolor sit amet, con sectetur adipiscing elit, sed do eiul ou esmod tempor incididunt ut lab ore et dolore magna aliqua.</p>
  </div>
  <div class="dots"><i></i><i class="on"></i><i></i></div>
</section>

<section class="about">
  <svg class="abs" style="left:0;top:1640px" width="1200" height="670" viewBox="0 0 1200 670">
    <path d="M0 60 C80 20 150 -5 260 50 C420 120 560 80 760 60 C960 40 1100 30 1200 60 L1200 640 C1000 670 760 660 560 640 C360 620 160 630 0 660 Z" fill="#f0f0f0"/>
  </svg>
  <div class="about-copy">
    <h2><span class="r">ABOUT TARROWBY</span><br>INSURANCE</h2>
    <p>Lorem ipsum dolor sit amet, consectetur adipiscinglit, sed do eiusmod tempor incididunt ut labore et dolore magna aliqua. Quis ipsum suspendisse ultrices gravi isus commodo viverra maecenas accumsan lacus vel facilisipsum suspendisse ultrices gravi isus commodo viverra maltrices gravi isuss.Lorem ipsum dolor sit amet, consectetur adipiscinglit, sed do .</p>
  </div>
  <span class="corner" style="left:490px;top:1808px"></span>
  <a class="btn" style="left:148px;top:2102px;width:183px">Request a quote</a>
  <svg class="abs" style="left:640px;top:1812px" width="390" height="385" viewBox="0 0 390 385">
    <circle cx="188" cy="192" r="188" fill="#c8102e"/>
  </svg>
  <div class="photo" role="img" aria-label="Cupped hands sheltering a toy blue truck" style="left:646px;top:1818px;width:370px;height:370px;border-radius:50%;background:radial-gradient(circle at 50% 40%,#ffffff,#f0e2d6 55%,#3f6fc4 80%,#e9ecf0)"></div>
</section>

<section class="why">
  <div class="why-copy">
    <div class="label">Why Choose Us?</div>
    <h2>Let us save you money on your commercial truck insurance.</h2>
  </div>
  <span class="corner" style="left:330px;top:2472px"></span>
  <a class="btn" style="left:145px;top:2762px;width:183px">Request a quote</a>

  <div class="feature" style="left:472px;top:2465px">
    <svg viewBox="0 0 24 24"><path fill="#c8102e" d="M19.4 13a7.6 7.6 0 0 0 0-2l2.1-1.6-2-3.5-2.5 1a7.7 7.7 0 0 0-1.7-1L15 3h-4l-.4 2.9a7.7 7.7 0 0 0-1.7 1l-2.5-1-2 3.5L6.6 11a7.6 7.6 0 0 0 0 2l-2.1 1.6 2 3.5 2.5-1a7.7 7.7 0 0 0 1.7 1L11 21h4l.4-2.9a7.7 7.7 0 0 0 1.7-1l2.5 1 2-3.5zM13 15.5a3.5 3.5 0 1 1 0-7 3.5 3.5 0 0 1 0 7z"/></svg>
    <h3>Experience</h3>
    <p>Lorem ipsum dolor lrewsit amet consectetur adip iscinglit, sedeius mod tempor incididunt ut lab</p>
  </div>
  <div class="feature" style="left:797px;top:2465px">
    <svg viewBox="0 0 24 24"><circle cx="12" cy="12" r="10" fill="#c8102e"/><path d="M12 6v6l4 3" stroke="#fff" stroke-width="2" fill="none"/></svg>
    <h3>Service</h3>
    <p>Lorem ipsum dolor lrewsit amet consectetur adip iscinglit, sedeius mod tempor incididunt ut lab</p>
  </div>
  <div class="feature" style="left:472px;top:2646px">
    <svg viewBox="0 0 24 24" fill="#c8102e"><circle cx="12" cy="7" r="3"/><circle cx="5" cy="9" r="2.3"/><circle cx="19" cy="9" r="2.3"/><path d="M6 20c0-4 2.7-7 6-7s6 3 6 7z"/><path d="M0 19c0-3 2-5 5-5 1 0 2 .3 2.5.8C6 16 5 18 5 19z"/><path d="M24 19c0-3-2-5-5-5-1 0-2 .3-2.5.8C18 16 19 18 19 19z"/></svg>
    <h3>Specialists</h3>
    <p>Lorem ipsum dolor lrewsit amet consectetur adip iscinglit, sedeius mod tempor incididunt ut lab</p>
  </div>
  <div class="feature" style="left:797px;top:2646px">
    <svg viewBox="0 0 24 24" fill="#c8102e"><circle cx="12" cy="7" r="4.5"/><path d="M3 22c0-5 4-8.5 9-8.5s9 3.5 9 8.5z"/></svg>
    <h3>Expertise</h3>
    <p>Lorem ipsum dolor lrewsit amet consectetur adip iscinglit, sedeius mod tempor incididunt ut lab</p>
  </div>
</section>

<section>
  <div class="quote-band photo" role="img" aria-label="Aerial view of white trucks driving on a highway through green countryside" style="background:linear-gradient(180deg,#5d6462 0%,#7a7f78 25%,#4c5a44 55%,#3f4541 100%)"></div>
  <h2 class="abs" style="left:148px;top:3175px;color:#fff;font-size:40px;line-height:50px;width:420px">DO YOU NEED AN INSURANCE QUOTE FOR YOUR COMMERCIAL TRUCK?</h2>
  <form class="quote-form">
    <div class="head">GET A FREE QUOTE</div>
    <div class="field" style="top:99px">Name:</div>
    <div class="field" style="top:155px">Phone:</div>
    <div class="field" style="top:212px">Email:</div>
    <div class="field msg" style="top:269px">Mesage:</div>
    <div class="submit">SUBMIT NOW</div>
  </form>
</section>

<section class="blog">
  <div class="blog-title">COMPANY BLOG NEWS</div>
  <span class="corner" style="left:774px;top:3724px"></span>
  <div class="photo" role="img" aria-label="Row of parked red trucks" style="left:150px;top:3858px;width:399px;height:345px;background:linear-gradient(135deg,#9aa3ad,#c41f26 35%,#7a1418 65%,#5a5f63)"></div>
  <div class="blog-feature"><h3>Lorem ipsum dolor sit amet consectetur adipiscing</h3></div>
  <div class="date abs" style="left:152px;top:4302px">March 30, 2023</div>

  <article class="post" style="top:3858px">
    <div class="thumb" role="img" aria-label="Blue truck on a highway" style="background:linear-gradient(135deg,#cfd6de,#3a5fb0 50%,#6b6f73)"></div>
    <h4>Lorem ipsum dolor sit amet<br>consectetur adipiscing</h4>
    <span class="date">March 30, 2023</span>
  </article>
  <article class="post" style="top:4020px">
    <div class="thumb" role="img" aria-label="Red truck at sunset" style="background:linear-gradient(180deg,#e3a76c,#b0302a 60%,#4a4a4a)"></div>
    <h4>Lorem ipsum dolor sit amet<br>consectetur adipiscing</h4>
    <span class="date">March 30, 2023</span>
  </article>
  <article class="post" style="top:4182px">
    <div class="thumb" role="img" aria-label="Hands signing an insurance document" style="background:linear-gradient(135deg,#f3f3f3,#d9c8bc 55%,#9eaac0)"></div>
    <h4>Lorem ipsum dolor sit amet<br>consectetur adipiscing</h4>
    <span class="date">March 30, 2023</span>
  </article>
</section>

<footer class="site-footer">
  <svg class="abs" style="left:0;top:0" width="1200" height="530" viewBox="0 0 1200 530">
    <path d="M0 10 C200 40 420 60 640 40 C860 20 1040 0 1200 30 L1200 120 L0 120 Z" fill="#f4c6cd"/>
    <path d="M0 50 C200 70 420 90 640 70 C860 50 1040 20 1200 50 L1200 120 L0 120 Z" fill="#c8102e"/>
    <path d="M0 80 C220 90 440 100 660 85 C880 70 1060 50 1200 65 L1200 530 L0 530 Z" fill="#1d2524"/>
    <line x1="150" y1="440" x2="1050" y2="440" stroke="#55605e" stroke-width="1"/>
  </svg>
</footer>
<div class="brand" style="left:152px;top:4690px;color:#fff;font-size:18px"><span class="dot"></span>TARROWBY INSURANCE</div>

<div class="foot-col" style="left:438px">
  <h5>MENU</h5>
  <ul><li>Home</li><li>About Us</li><li>Why CHose Us</li><li>Get A Quote</li><li>Testimonials</li><li>Contact</li></ul>
</div>
<div class="foot-col" style="left:580px">
  <h5>CONTACT</h5>
  <div class="contact-row"><span class="ico"><svg width="14" height="14" viewBox="0 0 24 24"><path fill="#fff" d="M12 2a7 7 0 0 0-7 7c0 5 7 13 7 13s7-8 7-13a7 7 0 0 0-7-7zm0 9.5A2.5 2.5 0 1 1 12 6.5a2.5 2.5 0 0 1 0 5z"/></svg></span><span>Lorem ipsum dolor sit<br>aloremm etconsectetur<br>adipiscig elit sed</span></div>
  <div class="contact-row"><span class="ico"><svg width="14" height="14" viewBox="0 0 24 24"><path fill="#fff" d="M6.6 10.8a15 15 0 0 0 6.6 6.6l2.2-2.2c.3-.3.7-.4 1-.2 1.1.4 2.3.6 3.6.6.6 0 1 .4 1 1V20c0 .6-.4 1-1 1A17 17 0 0 1 3 4c0-.6.4-1 1-1h3.5c.6 0 1 .4 1 1 0 1.3.2 2.5.6 3.6.1.3 0 .7-.2 1z"/></svg></span><span>Phone:<br>555-014-2270</span></div>
  <div class="contact-row"><span class="ico"><svg width="14" height="14" viewBox="0 0 24 24"><path fill="#fff" d="M2 5h20v14H2z M2 5l10 8 10-8" stroke="#c8102e" stroke-width="1.5"/></svg></span><span>Email:<br>hello@tarrowby-cover.com</span></div>
</div>
<div class="foot-col" style="left:810px;width:240px">
  <h5>NEWSLETTER</h5>
  <p style="font-size:12px;line-height:15px;color:#ddd">Lorem ipsum dolor sit am etconsectetur adipiscig elit sed do eiusmod tem por incididunt ut lablorore et dolore</p>
  <div style="margin-top:18px;height:38px;border-radius:19px;background:#fff;color:#555;font-size:11px;padding:13px 16px">Email:</div>
  <div style="margin-top:20px;height:38px;line-height:38px;border-radius:19px;background:var(--red);color:#fff;font-weight:700;font-size:14px;text-align:center">SUBMIT</div>
</div>
<div class="social"><i></i><i></i><i></i></div>
<div class="abs" style="left:822px;top:4860px;color:#fff;font-size:12px">Copyrights © 2023 All Rights Reversed</div>

</body>
</html>
```